Painting Company Business Card

Brightwell Painting needs a new business card. See attachments for our logo and current card as an example.
We want to utilize the same colors in the logo, and keep all the information that is currently on it. Just need an updated and modern design.
We are open to loosing the Association Logos if it means a better design.
We are also entertaining a spot for a picture of a headshot of the person listed on the card. Head shot can be finished later.

```html
<!DOCTYPE html>
<html lang="en">
<head>
<meta charset="utf-8">
<title>Brightwell Painting – Business Card</title>
<link href="https://fonts.googleapis.com/css2?family=Montserrat:ital,wght@0,400;0,600;0,700;1,700&display=swap" rel="stylesheet">
<style>
  :root {
    --green: #4b5a36;
    --maroon: #7b3a33;
    --paper: #f8f8f5;
    --ink: #2b2b2b;
    --badge: #3a3a3a;
    --tick: #6f8f7a;
    --backdrop: #ebebeb;
  }
  * { box-sizing: border-box; margin: 0; padding: 0; }
  html, body {
    width: 1200px; height: 801px; overflow: hidden;
    background: var(--backdrop);
    font-family: "Montserrat", sans-serif;
    color: var(--ink);
  }
  .canvas {
    position: relative; width: 1200px; height: 801px;
    display: flex; align-items: center; justify-content: center; gap: 40px;
  }
  .card {
    position: relative; width: 540px; height: 309px;
    background: var(--paper);
    border: 4px solid var(--green);
    box-shadow: 0 6px 18px rgba(0,0,0,0.12);
    overflow: hidden;
  }

  /* Front */
  .brand {
    position: absolute; left: 38px; top: 62px;
    display: flex; align-items: center; gap: 16px;
  }
  .brand-mark {
    width: 30px; height: 30px; background: var(--maroon);
  }
  .brand-name {
    font-weight: 600; font-size: 40px; line-height: 1.05;
    color: var(--green); letter-spacing: 0.5px;
  }
  .badges {
    position: absolute; left: 38px; right: 38px; bottom: 34px;
    display: flex; justify-content: space-between; align-items: center;
  }
  .badge { background: var(--badge); opacity: 0.85; }
  .badge--wide { width: 58px; height: 26px; border-radius: 3px; }
  .badge--square { width: 34px; height: 34px; }
  .badge--round { width: 36px; height: 36px; border-radius: 50%; }

  /* Back */
  .contact-person { position: absolute; left: 178px; top: 42px; }
  .person-name { font-weight: 700; font-size: 19px; }
  .person-title { font-weight: 700; font-style: italic; font-size: 14px; margin-top: 2px; }
  .services { list-style: none; margin-top: 14px; }
  .services li {
    display: flex; align-items: center; gap: 10px;
    font-size: 17px; line-height: 24px;
  }
  .services svg { width: 14px; height: 14px; flex: none; }
  .contact-band {
    position: absolute; left: 0; right: 0; bottom: 0; height: 86px;
    background: var(--green); color: #fff;
    display: flex; flex-direction: column; justify-content: center;
    padding-left: 38px; gap: 6px;
  }
  .contact-line { font-size: 16px; letter-spacing: 0.3px; }
  .website { font-size: 18px; font-weight: 700; }
</style>
</head>
<body>
<main class="canvas">

  <section class="card card--front" aria-label="Card front">
    <div class="brand">
      <span class="brand-mark"></span>
      <span class="brand-name">Brightwell<br>Painting</span>
    </div>
    <div class="badges" aria-label="Association memberships">
      <span class="badge badge--wide"></span>
      <span class="badge badge--square"></span>
      <span class="badge badge--round"></span>
      <span class="badge badge--square"></span>
      <span class="badge badge--wide"></span>
      <span class="badge badge--square"></span>
    </div>
  </section>

  <section class="card card--back" aria-label="Card back">
    <div class="contact-person">
      <p class="person-name">Daniel Harper</p>
      <p class="person-title">Quality Manager</p>
      <ul class="services">
        <li><svg viewBox="0 0 14 14"><circle cx="7" cy="7" r="6" fill="none" stroke="var(--tick)" stroke-width="1.3"/><path d="M4 7.2l2 2 4-4.2" fill="none" stroke="var(--tick)" stroke-width="1.5"/></svg>Exterior Painting</li>
        <li><svg viewBox="0 0 14 14"><circle cx="7" cy="7" r="6" fill="none" stroke="var(--tick)" stroke-width="1.3"/><path d="M4 7.2l2 2 4-4.2" fill="none" stroke="var(--tick)" stroke-width="1.5"/></svg>Interior Painting</li>
        <li><svg viewBox="0 0 14 14"><circle cx="7" cy="7" r="6" fill="none" stroke="var(--tick)" stroke-width="1.3"/><path d="M4 7.2l2 2 4-4.2" fill="none" stroke="var(--tick)" stroke-width="1.5"/></svg>Carpentry</li>
        <li><svg viewBox="0 0 14 14"><circle cx="7" cy="7" r="6" fill="none" stroke="var(--tick)" stroke-width="1.3"/><path d="M4 7.2l2 2 4-4.2" fill="none" stroke="var(--tick)" stroke-width="1.5"/></svg>Drywall</li>
      </ul>
    </div>
    <div class="contact-band">
      <p class="contact-line">555-201-4837 | Daniel.Brightwell@mailbox.com</p>
      <p class="website">BrightwellPainting.com</p>
    </div>
  </section>

</main>
</body>
</html>
```